Images and design ideas provided: Postcard size flier

2 sided postcard size flier to hand people on the street.

A FUN tax business needs a postcard size flier to hand people on the street. Not a typical serious, quiet, office so make the image fun!

Exact wording, logo and key images provided. You are free to add other images as you see fit (such as money).

Side 1: Use image of lady looking up (she should be looking at text provided).All spanish and english text provided. Logo in bottom right corner. Address at bottom of card.

Side 2: Image of lady holding money and pointing. Remove money and have her holding a sign/or some other creative way to have her looking at text. All spanish and english text provided. Logo in bottom right corner. Address at bottom of card.

Size: 4" x 6" horizontal or vertical is ok
Each side can be different and image/design does not have to be related.

Target Market(s)

Age 18-35

Industry/Entity Type

Accounting

Font styles to use
Sans Serif

Colors

Designer to choose colors to be used in the design.

Requirements
Must have
• Use text document provided. All text goes on both sides.
• Should be easy to read from a few feet away.
Nice to have
• Bright colors to attract attention of people walking by to grab flier/card. Images of money ok.
Should not have
• No images of calculators or typical accounting tax forms.

```html
<!DOCTYPE html>
<html lang="en">
<head>
<meta charset="utf-8">
<title>Refund Royale Postcards</title>
<link href="https://fonts.googleapis.com/css2?family=Source+Sans+3:wght@400;600;700;800&display=swap" rel="stylesheet">
<style>
  :root {
    --page: #161616;
    --red: #e92741;
    --red-deep: #b8203a;
    --blue: #3577c0;
    --blue-deep: #2a5f9c;
    --sky-light: #ffffff;
    --sky: #c9d6f0;
    --ink: #222222;
    --white: #ffffff;
  }
  html, body {
    margin: 0;
    width: 982px;
    height: 1200px;
    overflow: hidden;
    background: var(--page);
    font-family: "Source Sans 3", "Source Sans Pro", sans-serif;
  }
  .postcard {
    position: absolute;
    left: 127px;
    width: 727px;
    height: 485px;
    display: block;
  }
  .postcard--front { top: 101px; }
  .postcard--back { top: 619px; }
  .postcard text { font-family: "Source Sans 3", "Source Sans Pro", sans-serif; }
  .headline { font-weight: 800; fill: var(--white); }
  .subline { font-weight: 400; fill: var(--white); }
  .spanish { font-weight: 700; }
  .note { font-weight: 400; fill: var(--ink); }
  .brand { font-weight: 700; }
  .address { font-weight: 400; fill: var(--ink); }
  .phone { font-weight: 700; fill: var(--ink); }
</style>
</head>
<body>

<svg class="postcard postcard--front" viewBox="0 0 727 485" xmlns="http://www.w3.org/2000/svg">
  <defs>
    <linearGradient id="sky-front" x1="0" y1="0" x2="0.3" y2="1">
      <stop offset="0" stop-color="var(--sky-light)"/>
      <stop offset="1" stop-color="var(--sky)"/>
    </linearGradient>
    <linearGradient id="photo-front" x1="0" y1="0" x2="0" y2="1">
      <stop offset="0" stop-color="#c8a86a" stop-opacity="0.55"/>
      <stop offset="0.5" stop-color="#8a8f5e" stop-opacity="0.6"/>
      <stop offset="1" stop-color="#7d7a50" stop-opacity="0.7"/>
    </linearGradient>
  </defs>
  <rect class="card-sky" width="727" height="485" fill="url(#sky-front)"/>
  <path class="wave-shadow" d="M0 0H727V160C520 150 220 200 0 295Z" fill="var(--red-deep)"/>
  <path class="wave-band" d="M0 0H727V144C510 140 220 175 0 262Z" fill="var(--red)"/>
  <rect class="photo" x="12" y="180" width="350" height="305" rx="40" fill="url(#photo-front)" role="img" aria-label="Photo of a smiling woman in a king costume and crown looking up at the text with arms raised"/>

  <text class="headline" x="363" y="78" text-anchor="middle" font-size="61">Get $100 Cash Now!</text>
  <text class="subline" x="363" y="123" text-anchor="middle" font-size="37">with paid tax preparation</text>

  <text class="spanish" x="686" y="215" text-anchor="end" font-size="42" fill="var(--blue)">!Reciba <tspan fill="var(--red)">$100</tspan> en</text>
  <text class="spanish" x="686" y="263" text-anchor="end" font-size="42" fill="var(--blue)">efectivo ahora!</text>
  <text class="note" x="523" y="293" text-anchor="middle" font-size="19">con la preparacion pagada</text>
  <text class="note" x="523" y="319" text-anchor="middle" font-size="19">de sus impuestos</text>

  <rect class="brand-mark" x="418" y="355" width="26" height="26" fill="var(--blue)"/>
  <text class="brand" x="454" y="378" font-size="30" fill="var(--red)">Refund Royale</text>
  <text class="address" x="686" y="419" text-anchor="end" font-size="16">418 Harbor Ave. Bronx NY 10455</text>
  <text class="phone" x="686" y="459" text-anchor="end" font-size="37">(718) 555-0148</text>
</svg>

<svg class="postcard postcard--back" viewBox="0 0 727 485" xmlns="http://www.w3.org/2000/svg">
  <defs>
    <linearGradient id="sky-back" x1="0" y1="0" x2="0.3" y2="1">
      <stop offset="0" stop-color="var(--sky-light)"/>
      <stop offset="1" stop-color="var(--sky)"/>
    </linearGradient>
    <linearGradient id="photo-back" x1="0" y1="0" x2="0" y2="1">
      <stop offset="0" stop-color="#d0a24a" stop-opacity="0.75"/>
      <stop offset="0.45" stop-color="#b08a6a" stop-opacity="0.7"/>
      <stop offset="1" stop-color="#7f8458" stop-opacity="0.75"/>
    </linearGradient>
  </defs>
  <rect class="card-sky" width="727" height="485" fill="url(#sky-back)"/>
  <path class="wave-shadow" d="M0 0H727V143C520 125 230 150 0 240Z" fill="var(--blue-deep)"/>
  <path class="wave-band" d="M0 0H727V136C520 118 230 140 0 229Z" fill="var(--blue)"/>
  <rect class="photo" x="0" y="0" width="292" height="485" rx="36" fill="url(#photo-back)" role="img" aria-label="Photo of a smiling woman in a king costume and crown holding a fan of cash toward the viewer"/>

  <text class="headline" x="461" y="63" text-anchor="middle" font-size="45">Get $100 Cash Now!</text>
  <text class="subline" x="461" y="101" text-anchor="middle" font-size="32">with paid tax preparation</text>

  <text class="spanish" x="690" y="210" text-anchor="end" font-size="50" fill="var(--red)">!Reciba <tspan fill="var(--blue)">$100</tspan> en</text>
  <text class="spanish" x="690" y="262" text-anchor="end" font-size="50" fill="var(--red)">efectivo ahora!</text>
  <text class="note" x="513" y="299" text-anchor="middle" font-size="21">con la preparacion pagada</text>
  <text class="note" x="513" y="328" text-anchor="middle" font-size="21">de sus impuestos</text>

  <rect class="brand-mark" x="422" y="357" width="26" height="26" fill="var(--blue)"/>
  <text class="brand" x="458" y="380" font-size="30" fill="var(--red)">Refund Royale</text>
  <text class="address" x="690" y="421" text-anchor="end" font-size="16">418 Harbor Ave. Bronx NY 10455</text>
  <text class="phone" x="690" y="461" text-anchor="end" font-size="37">(718) 555-0148</text>
</svg>

</body>
</html>
```